Design a Crossfit Flyer to attract new membership

With constantly updating workouts and the nutritional help Tollmere Ironworks is more than just an average gym. It’s a place for everyone to get healthy in a stress-free, safe and friendly environment.

Target Market(s)

Women ages 25-60 years old

Industry/Entity Type

Environment

Font styles to use
Serif

Requirements
Must have
• Please read thru the following info before you begin your design:
• Crossfit Flyer Information
• Please keep in mind a few things:
• 1) Our facility colors orange and green (you can see from my website what the color scheme is)
• 2) Our target demo graphic is women between the ages of 25-60, a large majority of my current clientele are middle aged women 45-60 years old
• 3) Try to keep it clean, and white (like quills website) if possible
• Side 1: (image of equipment and a younger women working out)
• 1) TMIW Logo
• 2) FREE WEEK TRIAL (big font) Sing up at www.tmironworks.net/schedulesign-up
• 3) Schedule: Monday-Friday 5:30am – 6:15am – 6:00pm – 7:00pm
• 4) Rates: $150/ Month Unlimited Classes - $100 /10 session package
• *15% discount for all fire, police, military, veterans, teachers, current students & trade association members
• 5) Address: 217 Pell Avenue Staten Island, NY 10308
• 6) Contact info: Phone: 347-518-7064 Email: tmironworks@mailbox.example
• 7) Website and Social media www.tmironworks.net find us @TMIronworks on Facebook, Twitter, Instagram, Yelp, Google + and foursquare
• Side 2 (image of a women working out, preferable middle aged):
• 1) 6 Benefits of CrossFit:
• a. Benefit #1: It BLASTS calories
• b. Benefit #2: It’s great Cardiovascular conditioning
• c. Benefit #3: It increases joint mobility
• d. Benefit #4: Everyday is something different, guaranteed
• e. Benefit #5: You’ll make new friends
• f. Benefit #6: You’ll feel like a badass
• 2) Free Week Trial Class (smaller font at the bottom) sign up at: www.tmironworks.net/schedulesign-up

```html
<!DOCTYPE html>
<html lang="en">
<head>
<meta charset="utf-8">
<title>Tollmere Ironworks – Free Week Trial</title>
<link rel="stylesheet" href="https://fonts.googleapis.com/css2?family=Arimo:wght@400;700&display=swap">
<style>
  :root {
    --orange: #f8a108;
    --green: #1f4a1c;
    --white: #ffffff;
    --photo-light: #d9dcd8;
    --photo-mid: #a9aca6;
    --photo-dark: #3d3f3e;
  }
  html, body {
    margin: 0;
    padding: 0;
    overflow: hidden;
    background: #ffffff;
  }
  .flyer {
    position: relative;
    width: 1200px;
    height: 930px;
    background: var(--orange);
    overflow: hidden;
    font-family: "Arimo", Arial, sans-serif;
    color: var(--green);
  }
  .flyer > * { position: absolute; margin: 0; line-height: 1; white-space: nowrap; }

  .brand {
    left: 48px; top: 62px;
    width: 220px;
    font-size: 38px;
    font-weight: 700;
    line-height: 1.05;
    white-space: normal;
    color: var(--green);
    letter-spacing: 0.5px;
  }
  .headline {
    left: 310px; top: 42px;
    font-size: 84px;
    font-weight: 400;
    color: var(--white);
    letter-spacing: 3px;
  }
  .signup {
    left: 301px; top: 125px;
    font-size: 33px;
    letter-spacing: 0.8px;
  }
  .hero-photo { left: 0; top: 0; }

  .schedule { left: 60px; top: 210px; font-size: 35px; letter-spacing: 0.8px; }
  .times { left: 55px; top: 261px; font-size: 22px; letter-spacing: 0.5px; }
  .rates { left: 95px; top: 307px; font-size: 24px; }
  .rates .price { font-size: 44px; letter-spacing: 0.5px; margin-left: 6px; }
  .unlimited { left: 92px; top: 402px; font-size: 41px; font-weight: 700; letter-spacing: 0.5px; }
  .package { left: 80px; top: 455px; font-size: 29px; letter-spacing: 0.6px; }

  .address { left: 58px; top: 577px; font-size: 23px; line-height: 32px; white-space: normal; width: 520px; letter-spacing: 0.4px; }
  .contact-label { left: 57px; top: 648px; font-size: 25px; letter-spacing: 0.4px; }
  .phone { left: 57px; top: 682px; font-size: 25px; letter-spacing: 0.4px; }
  .email { left: 57px; top: 719px; font-size: 25px; letter-spacing: 0.4px; }
  .website { left: 57px; top: 762px; font-size: 23px; letter-spacing: 0.4px; }
  .social-handle { left: 57px; top: 800px; font-size: 24px; letter-spacing: 0.4px; }
  .strong { font-weight: 700; }

  .social-row { left: 55px; top: 851px; display: flex; gap: 18px; }
  .social-row span { display: block; width: 36px; height: 36px; border-radius: 50%; background: var(--green); }

  .footnote {
    right: 40px; top: 842px;
    font-size: 21px;
    line-height: 23px;
    text-align: right;
    letter-spacing: 0.3px;
  }
</style>
</head>
<body>
<main class="flyer">
  <div class="brand">Tollmere Ironworks</div>

  <h1 class="headline">FREE WEEK TRIAL</h1>
  <p class="signup">Sign up at www.tmironworks.net/schedulesign-up</p>

  <svg class="hero-photo" width="1200" height="930" viewBox="0 0 1200 930" role="img" aria-label="Photo of a young woman lifting a barbell overhead in a tiled gym">
    <defs>
      <linearGradient id="photo-tone" x1="0" y1="0" x2="1" y2="1">
        <stop offset="0" stop-color="var(--photo-light)"/>
        <stop offset="0.55" stop-color="var(--photo-mid)"/>
        <stop offset="1" stop-color="var(--photo-dark)"/>
      </linearGradient>
      <clipPath id="photo-shape">
        <circle cx="925" cy="497" r="337"/>
      </clipPath>
    </defs>
    <rect x="588" y="170" width="612" height="655" fill="url(#photo-tone)" clip-path="url(#photo-shape)"/>
    <rect x="1000" y="170" width="200" height="655" fill="url(#photo-tone)"/>
  </svg>

  <p class="schedule">Schedule: Monday-Friday</p>
  <p class="times">5:30am I 6:15am I 6:00pm I 7:00pm</p>
  <p class="rates">Rates: <span class="price">$150/ Month*</span></p>
  <p class="unlimited">Unlimited Classes</p>
  <p class="package">$100 /10 session package</p>

  <p class="address">Address: 217 Pell Avenue Staten Island, NY 10308</p>
  <p class="contact-label">Contact info:</p>
  <p class="phone">Phone: <span class="strong">347-518-7064</span></p>
  <p class="email">Email: <span class="strong">tmironworks@mailbox.example</span></p>
  <p class="website">Website : <span class="strong">www.tmironworks.net</span></p>
  <p class="social-handle">Find us <span class="strong">@TMIronworks on</span></p>

  <div class="social-row" aria-label="Social channels">
    <span></span><span></span><span></span><span></span><span></span><span></span>
  </div>

  <p class="footnote">*15% discount for all fire, police, military, veterans,<br>teachers,current students &amp; trade association members</p>
</main>
</body>
</html>
```